Varnath Consulting Business card design.

See our website www.varnathconsulting-example.com which will give you a good idea of what we are about. The font is called 'Play'.

I'd like a standout business card in keeping with the themes and branding on the website

Target Market(s)

professionals. HR directors

Industry/Entity Type

Business

Contact Information for Business Card

Varnath Consulting PO Box 3917 Tindale Creek NSW 2840 1300 457 318 Gerald Ashbury Principal email: jobs@varnathconsulting-example.com ABN: 31792048663

Font styles to use
Other font styles liked:
• Play

Requirements
Must have
• Must have same design colours and branding as website.
• On back I'd prefer a list of the things we do which appears below the name at the header on the website

```html
<!DOCTYPE html>
<html lang="en">
<head>
<meta charset="utf-8">
<title>Varnath Consulting – Business Card</title>
<link href="https://fonts.googleapis.com/css2?family=Play:wght@400;700&display=swap" rel="stylesheet">
<style>
  :root {
    --navy: #132a40;
    --blue: #2a93dc;
    --white: #ffffff;
    --paper: #f6f6f6;
    --ink: #1c2a38;
    --backdrop: #a9a6a6;
  }
  * { box-sizing: border-box; margin: 0; padding: 0; }
  html, body {
    width: 1200px;
    height: 1200px;
    overflow: hidden;
    background: var(--backdrop);
    font-family: "Play", sans-serif;
  }
  .card {
    position: absolute;
    left: 243px;
    width: 714px;
    height: 420px;
  }

  /* Front */
  .card-front { top: 116px; background: var(--navy); }
  .front-name {
    position: absolute;
    top: 128px;
    left: 0;
    width: 100%;
    text-align: center;
    font-size: 54px;
    line-height: 1;
    font-weight: 400;
    color: var(--white);
    letter-spacing: 0.5px;
    white-space: nowrap;
  }
  .front-services {
    position: absolute;
    top: 191px;
    left: 0;
    width: 100%;
    text-align: center;
    font-size: 15px;
    letter-spacing: 2.4px;
    color: var(--blue);
    white-space: nowrap;
  }
  .front-web {
    position: absolute;
    top: 346px;
    left: 0;
    width: 100%;
    display: flex;
    justify-content: center;
    align-items: center;
    gap: 14px;
    font-size: 18px;
    color: var(--white);
  }
  .front-web .accent { color: var(--blue); }
  .front-web .rule { width: 34px; height: 2px; background: var(--blue); border-radius: 2px; }

  /* Back */
  .card-back { top: 644px; background: var(--paper); }
  .back-name {
    position: absolute;
    left: 46px;
    top: 134px;
    width: 270px;
    font-size: 44px;
    line-height: 54px;
    font-weight: 400;
    color: var(--navy);
    letter-spacing: 0.5px;
    white-space: nowrap;
  }
  .contact {
    position: absolute;
    left: 353px;
    top: 84px;
    color: var(--ink);
  }
  .contact-person {
    font-size: 23px;
    font-weight: 700;
    color: var(--blue);
    line-height: 30px;
  }
  .contact-role { font-size: 16px; line-height: 24px; margin-bottom: 10px; }
  .contact-line {
    display: flex;
    align-items: center;
    gap: 14px;
    font-size: 17.5px;
    line-height: 26px;
    white-space: nowrap;
  }
  .contact-line svg { width: 20px; height: 16px; flex: none; }
  .contact-abn { font-size: 17.5px; line-height: 28px; margin-top: 4px; }
  .contact-abn .label { color: var(--blue); }
  .contact-address { font-size: 17.5px; line-height: 26px; white-space: nowrap; }
  .service-band {
    position: absolute;
    left: 0;
    bottom: 0;
    width: 100%;
    height: 51px;
    background: var(--navy);
    color: var(--white);
    font-size: 18px;
    letter-spacing: 1.2px;
    display: flex;
    align-items: center;
    justify-content: center;
    white-space: nowrap;
  }
</style>
</head>
<body>

<section class="card card-front">
  <h1 class="front-name">VARNATH CONSULTING</h1>
  <p class="front-services">Search &amp; Select | Career | Coaching | Leadership | Outplacement</p>
  <p class="front-web">
    <span class="rule"></span>
    <span>www.<span class="accent">varnathconsulting-example</span>.com</span>
    <span class="rule"></span>
  </p>
</section>

<section class="card card-back">
  <h2 class="back-name">VARNATH<br>CONSULTING</h2>

  <div class="contact">
    <p class="contact-person">Gerald Ashbury</p>
    <p class="contact-role">Principal</p>

    <p class="contact-line">
      <svg viewBox="0 0 20 16" aria-hidden="true">
        <path d="M2 5 Q10 -1 18 5 L16 7 L13 5.5 L13 4 Q10 3 7 4 L7 5.5 L4 7 Z" fill="var(--blue)"/>
        <path d="M5 8 L15 8 L17 15 L3 15 Z" fill="var(--blue)"/>
        <circle cx="10" cy="11" r="2" fill="var(--paper)"/>
      </svg>
      <span>1300 457 318</span>
    </p>
    <p class="contact-line">
      <svg viewBox="0 0 20 16" aria-hidden="true">
        <circle cx="10" cy="8" r="7" fill="none" stroke="var(--blue)" stroke-width="1.6"/>
        <ellipse cx="10" cy="8" rx="3" ry="7" fill="none" stroke="var(--blue)" stroke-width="1.4"/>
        <line x1="3" y1="8" x2="17" y2="8" stroke="var(--blue)" stroke-width="1.4"/>
        <line x1="4.5" y1="4.5" x2="15.5" y2="4.5" stroke="var(--blue)" stroke-width="1.2"/>
        <line x1="4.5" y1="11.5" x2="15.5" y2="11.5" stroke="var(--blue)" stroke-width="1.2"/>
      </svg>
      <span>www.varnathconsulting-example.com</span>
    </p>
    <p class="contact-line">
      <svg viewBox="0 0 20 16" aria-hidden="true">
        <rect x="1" y="2" width="18" height="12" fill="var(--blue)"/>
        <path d="M1.5 2.5 L10 9 L18.5 2.5" fill="none" stroke="var(--paper)" stroke-width="1.4"/>
        <path d="M1.5 13.5 L7.5 7.5 M18.5 13.5 L12.5 7.5" fill="none" stroke="var(--paper)" stroke-width="1.2"/>
      </svg>
      <span>jobs@varnathconsulting-example.com</span>
    </p>

    <p class="contact-abn"><span class="label">ABN:</span> 31792048663</p>
    <p class="contact-address">PO Box 3917 Tindale Creek NSW 2840</p>
  </div>

  <p class="service-band">Search &amp; Select | Career | Coaching | Leadership | Outplacement</p>
</section>

</body>
</html>
```